I am a pastry chef and just started my own business. I make all sorts of pastries: french macarons, petit fours, artisan chocolates, artisan bread, and they can be ordered on the website. I'm obsessed with Wonderland, so I'd like to have a logo & a background that incorporate that, something whimsical. I was thinking of a white rabbit wearing a chef toque - maybe he could have a monocle on. The logo could go on one side of the business card with "Sugar Fox Patisserie Co" on a banner of some sort at the bottom, and the contact & info could go on the other side. I'd like a really light color as the background, maybe a really light yellow.

Industry/Entity Type

Chef

Contact Information for Business Card

Sugar Fox Patisserie Co
Mira Delcour Penhale
sugarfoxpatisserieco.shopvaleo.example
sugarfoxpatisserieco@mailvaleo.example
514-83-2071

```html
<!DOCTYPE html>
<html lang="en">
<head>
<meta charset="utf-8">
<title>Sugar Fox Patisserie Co — Business Card</title>
<link href="https://fonts.googleapis.com/css2?family=Comic+Neue:wght@400;700&display=swap" rel="stylesheet">
<style>
  :root {
    --stage: #ecebe4;
    --card-light: #f6f5c6;
    --card-mid: #efeda9;
    --card-deep: #e4e190;
    --band: #f9f8dc;
    --teal: #1f8f8e;
    --ink: #2b2a22;
    --url-ink: #5d5c40;
    --photo-cream: #e6e1d4;
    --photo-green: #b9bf6e;
    --photo-rose: #d9877f;
    --photo-blue: #9fc7c9;
    --mark: #dcd9a0;
  }
  * { box-sizing: border-box; margin: 0; padding: 0; }
  html, body { width: 1200px; height: 900px; overflow: hidden; }
  body {
    background: var(--stage);
    font-family: "Comic Neue", "Comic Sans MS", cursive;
    color: var(--ink);
    position: relative;
  }
  .card {
    position: absolute;
    left: 260px;
    width: 680px;
    height: 390px;
    background: linear-gradient(135deg, var(--card-light) 0%, var(--card-mid) 60%, var(--card-deep) 100%);
    box-shadow: 0 6px 18px rgba(0,0,0,.18);
    overflow: hidden;
  }
  .card--contact { top: 45px; }
  .card--brand { top: 465px; }

  /* contact side */
  .photo-strip {
    position: absolute;
    top: 0; left: 0; right: 0;
    height: 170px;
    display: flex;
    gap: 6px;
  }
  .photo {
    flex: 1;
    height: 100%;
  }
  .photo--cups { background: linear-gradient(160deg, var(--photo-blue), var(--photo-cream)); }
  .photo--cakes { background: linear-gradient(160deg, var(--photo-rose), #6b4a3a); }
  .photo--macarons { background: linear-gradient(160deg, var(--photo-green), var(--photo-cream)); }
  .photo--truffles { background: linear-gradient(160deg, var(--photo-cream), #9c8a70); }

  .contact {
    position: absolute;
    top: 195px;
    left: 60px;
    right: 40px;
  }
  .contact__name {
    font-size: 34px;
    font-weight: 400;
    color: var(--teal);
    margin-left: 40px;
    margin-bottom: 18px;
    letter-spacing: .5px;
  }
  .contact__line {
    font-size: 19px;
    line-height: 1.65;
    white-space: nowrap;
  }

  /* brand side */
  .brand-band {
    position: absolute;
    left: 60px;
    right: 0;
    top: 150px;
    height: 170px;
    background: var(--band);
  }
  .brand-mark {
    position: absolute;
    left: 110px;
    top: 30px;
    width: 110px;
    height: 110px;
    border-radius: 50%;
    background: var(--mark);
  }
  .brand-name {
    position: absolute;
    left: 230px;
    top: 180px;
    font-size: 50px;
    font-weight: 700;
    line-height: 1.05;
    color: var(--teal);
    letter-spacing: 1px;
  }
  .brand-url {
    position: absolute;
    left: 18px;
    bottom: 14px;
    font-size: 14px;
    font-style: normal;
    color: var(--url-ink);
  }
</style>
</head>
<body>

  <section class="card card--contact" aria-label="Contact side">
    <div class="photo-strip">
      <div class="photo photo--cups" role="img" aria-label="Photo of macaron topiary and teacup dessert display"></div>
      <div class="photo photo--cakes" role="img" aria-label="Photo of glazed pink and chocolate bundt cakes"></div>
      <div class="photo photo--macarons" role="img" aria-label="Photo of pistachio and coconut cookies"></div>
      <div class="photo photo--truffles" role="img" aria-label="Photo of artisan chocolates in paper cups"></div>
    </div>
    <div class="contact">
      <h1 class="contact__name">Mira Delcour Penhale</h1>
      <p class="contact__line">Web : www.sugarfoxpatisserieco.shopvaleo.example</p>
      <p class="contact__line">Email : sugarfoxpatisserieco@mailvaleo.example</p>
      <p class="contact__line">Phone : 514-83-2071</p>
    </div>
  </section>

  <section class="card card--brand" aria-label="Brand side">
    <div class="brand-band"></div>
    <div class="brand-mark"></div>
    <p class="brand-name">Sugar Fox<br>Patisserie Co</p>
    <p class="brand-url">sugarfoxpatisserieco.shopvaleo.example</p>
  </section>

</body>
</html>
```